Reaching the Root: Reasoning in Clinical Choice-Making

I'd like a cover that looks like it would fit on the shelf next to "The Symptom Mirage" by Harold Vintner, "The Fall of Forgetting" by Carl Mortenson, "Meal Mend" by Neil Forsby, "The Energy Renewal Plan" by Owen Prichardson or "The Gland Renewal Plan" by the same or "The Cortex Renewal Plan" by the same ... either text only (with some interesting fonts that make the title stand out, and the subtitle smaller) or a relevant image, though I'm not entirely sure what that would be since this is a book about big-picture medical decision making.
Author name is Dr Miriam Oakhurst, NMD
I'll eventually request an e-book, paperback, and audio cover from the winner...

Target Market(s)

practicing physicians

Industry/Entity Type

medicine

Requirements
Must have
• look similar to other books in the genre

```html
<!DOCTYPE html>
<html lang="en">
<head>
<meta charset="utf-8">
<title>Reaching the Root — Book Cover</title>
<link rel="stylesheet" href="https://fonts.googleapis.com/css2?family=Bebas+Neue&family=Playfair+Display:wght@400;500&display=swap">
<style>
  :root {
    --backdrop: #474747;
    --paper: #ffffff;
    --navy: #27286a;
    --blue: #1c6bb5;
    --mid-blue: #22549a;
    --gold: #e0b726;
    --white: #ffffff;
  }
  * { margin: 0; padding: 0; box-sizing: border-box; }
  html, body {
    width: 1200px;
    height: 1200px;
    overflow: hidden;
    background: var(--backdrop);
  }
  .cover {
    position: absolute;
    left: 240px;
    top: 60px;
    width: 720px;
    height: 1080px;
    background: var(--paper);
  }
  .title-lead {
    position: absolute;
    top: 134px;
    left: 0;
    width: 100%;
    text-align: center;
    font-family: "Bebas Neue", "Oswald", sans-serif;
    font-size: 128px;
    line-height: 1;
    letter-spacing: 5px;
    background: linear-gradient(90deg, var(--blue) 10%, var(--navy) 90%);
    -webkit-background-clip: text;
    background-clip: text;
    color: transparent;
  }
  .title-main {
    position: absolute;
    top: 220px;
    left: 0;
    width: 720px;
    height: 330px;
  }
  .subtitle-band {
    position: absolute;
    top: 642px;
    left: 0;
    width: 100%;
    height: 150px;
    background: linear-gradient(100deg, var(--blue) 15%, var(--mid-blue) 45%, var(--navy) 85%);
    border-top: 1px solid #123a6a;
    border-bottom: 1px solid #111;
    display: flex;
    align-items: center;
    justify-content: center;
  }
  .subtitle {
    font-family: "Playfair Display", "Georgia", serif;
    font-weight: 400;
    font-size: 45px;
    line-height: 62px;
    color: var(--white);
    text-align: center;
    letter-spacing: 0.5px;
  }
  .author {
    position: absolute;
    top: 978px;
    left: 0;
    width: 100%;
    text-align: center;
    font-family: "Bebas Neue", "Oswald", sans-serif;
    font-size: 54px;
    line-height: 1;
    letter-spacing: 3px;
    background: linear-gradient(90deg, var(--blue) 20%, var(--navy) 75%);
    -webkit-background-clip: text;
    background-clip: text;
    color: transparent;
  }
</style>
</head>
<body>
  <main class="cover">
    <h1 class="title">
      <span class="title-lead">Reaching the</span>
      <svg class="title-main" viewBox="0 0 720 330" aria-label="Root">
        <defs>
          <linearGradient id="title-gradient" x1="0" y1="0" x2="1" y2="0">
            <stop offset="0" stop-color="#27286a"/>
            <stop offset="0.55" stop-color="#2160a6"/>
            <stop offset="1" stop-color="#1c6bb5"/>
          </linearGradient>
        </defs>
        <text x="32" y="270" textLength="620" lengthAdjust="spacingAndGlyphs"
              font-family="'Playfair Display', Georgia, serif" font-size="282"
              fill="url(#title-gradient)">ROOT</text>
        <circle class="title-dot" cx="690" cy="250" r="21" fill="#e0b726"/>
      </svg>
    </h1>

    <section class="subtitle-band">
      <p class="subtitle">Reasoning in Clinical<br>Choice-Making</p>
    </section>

    <p class="author">Dr Miriam Oakhurst, NMD</p>
  </main>
</body>
</html>
```